Lanterns Over The Quiet Meadow Waters Book Cover

Book cover for a new book titled "Lanterns Over The Quiet Meadow Waters" which will show how retirees can pay NO tax in their retirement. Would like you to use your creative inspiration to come up with a design.

Please make MEADOW WATERS the emphasis of the title.

can you show money being rescued, or freed, from taxes.

I'm trying convey the message that retirees can FREE themselves from the burden of taxes in retirement by reading this book and following the instructions. Think about a person swimming with a weight on his back, sinking him. Suddenly the weight is removed. The feeling and imagery of the load being light now

Doing MEADOW WATERS can alleviate many of unnecessary taxes which will weight retirees down. But, unfortunately, many advisors in my industry do not educate their clients on this stuff.

Not a fan of dark backgrounds, generally speaking. Lighter is good.

Remember folks, go to brindlecart. Type in Roth IRA books. what will jump out over the stuff that's already there? Thanks!

Target Market(s)

recent, or soon to be, retirees, people in their 50s and 60s, typically couples

Industry/Entity Type

Financial

Font styles to use
Serif

Colors

Designer to choose colors to be used in the design.

Requirements
Must have
• Be optimistic, sunny, happy. How you do that? I don't know, that's why I'm hiring you. This book is designed for the lay person, (average Joe and Jane)
• Put my picture on the lower back.
• My name at bottom of the cover
Nice to have
• Be nice to have the cover POP on Brindlecart because I'm competing with so many other books and thumbnails
• Maybe a kite with a dollar bill that is breaking from a ball and chain? Just an idea.
Should not have
• No guys in suits. Happy couples sitting on the beach or sailing. That stuff is in every piece of financial planning literature.
• NOT TECHNICAL. NO PIGGY BANKS Design please

```html
<!DOCTYPE html>
<html lang="en">
<head>
<meta charset="utf-8">
<title>Lanterns Over The Quiet Meadow Waters – Book Cover</title>
<link rel="stylesheet" href="https://fonts.googleapis.com/css2?family=Bebas+Neue&family=Quicksand:wght@500&family=Montserrat:wght@500;700&family=Open+Sans:wght@400&display=swap">
<style>
  :root {
    --sky-deep: #1e4c96;
    --sky-mid: #7fa3cf;
    --sky-pale: #e9eef2;
    --haze-warm: #f3e2a8;
    --ink-navy: #1c3f78;
    --ink-title: #1e4f9a;
    --ink-dark: #1f2328;
    --ink-body: #3a3d42;
    --brand-teal: #2aa0a6;
    --balloon-red: rgba(214, 52, 40, 0.85);
    --balloon-soft: rgba(236, 140, 120, 0.45);
    --portrait-blue: #2f5fb8;
    --rule: #8a8f95;
  }
  * { margin: 0; padding: 0; box-sizing: border-box; }
  html, body { width: 1200px; height: 875px; overflow: hidden; background: #ffffff; }
  .cover {
    position: relative;
    width: 1200px;
    height: 875px;
    overflow: hidden;
  }
  .sky {
    position: absolute; inset: 0;
    background:
      radial-gradient(ellipse 60% 45% at 92% 92%, var(--haze-warm) 0%, rgba(243,226,168,0) 70%),
      radial-gradient(ellipse 70% 50% at 30% 30%, rgba(255,255,255,0.55) 0%, rgba(255,255,255,0) 70%),
      linear-gradient(170deg, var(--sky-deep) 0%, var(--sky-mid) 22%, var(--sky-pale) 52%, #f1f1ec 100%);
  }
  .balloon-area {
    position: absolute;
    left: 790px; top: 0;
    width: 360px; height: 430px;
    background: radial-gradient(ellipse 50% 48% at 52% 34%, var(--balloon-red) 0%, var(--balloon-soft) 60%, rgba(236,140,120,0) 100%);
  }
  .spine-title {
    position: absolute;
    left: 610px; top: 140px;
    transform-origin: 0 0;
    transform: rotate(90deg);
    font-family: "Bebas Neue", sans-serif;
    font-size: 29px;
    letter-spacing: 1.6px;
    line-height: 1;
    color: var(--ink-navy);
    white-space: nowrap;
  }
  .author-portrait {
    position: absolute;
    left: 60px; top: 478px;
    width: 156px; height: 156px;
    border-radius: 50%;
    background: radial-gradient(circle at 50% 40%, #4a78c8 0%, var(--portrait-blue) 70%);
    border: 3px solid #ffffff;
  }
  .author-bio {
    position: absolute;
    left: 234px; top: 506px;
    width: 302px;
    font-family: "Open Sans", sans-serif;
    font-size: 13.4px;
    line-height: 1.32;
    color: var(--ink-body);
  }
  .publisher-mark {
    position: absolute;
    left: 72px; top: 790px;
    display: flex; align-items: center; gap: 10px;
  }
  .publisher-dot {
    width: 34px; height: 34px; border-radius: 50%;
    background: var(--brand-teal);
  }
  .publisher-name {
    font-family: "Open Sans", sans-serif;
    font-size: 18px;
    color: var(--brand-teal);
    letter-spacing: 0.5px;
  }
  .front-title {
    position: absolute;
    left: 656px; width: 500px;
    top: 438px;
    text-align: center;
    font-weight: normal;
  }
  .title-lead {
    display: block;
    font-family: "Quicksand", sans-serif;
    font-weight: 500;
    font-size: 38px;
    color: var(--ink-navy);
    line-height: 1;
    white-space: nowrap;
  }
  .title-emphasis {
    display: block;
    font-family: "Bebas Neue", sans-serif;
    color: var(--ink-title);
    letter-spacing: 2px;
    white-space: nowrap;
  }
  .title-emphasis-main { font-size: 162px; line-height: 0.86; margin-top: 26px; }
  .title-emphasis-sub { font-size: 104px; line-height: 0.9; margin-top: 4px; }
  .author-block {
    position: absolute;
    left: 701px; width: 400px;
    top: 784px;
    text-align: center;
  }
  .author-name {
    display: inline-block;
    font-family: "Montserrat", sans-serif;
    font-weight: 700;
    font-size: 30px;
    line-height: 1.1;
    letter-spacing: 1.5px;
    color: var(--ink-dark);
    padding: 4px 6px;
    border-top: 1px solid var(--rule);
    border-bottom: 1px solid var(--rule);
    white-space: nowrap;
  }
  .author-site {
    font-family: "Montserrat", sans-serif;
    font-weight: 500;
    font-size: 15px;
    color: var(--ink-dark);
    margin-top: 6px;
  }
</style>
</head>
<body>
<main class="cover">
  <div class="sky" role="img" aria-label="Bright blue sky with soft white clouds fading to warm sunlight"></div>

  <div class="balloon-area" role="img" aria-label="Red and white striped hot air balloon rising as it drops small weights from its basket"></div>

  <div class="spine-title">LANTERNS OVER THE QUIET MEADOW WATERS</div>

  <div class="author-portrait" role="img" aria-label="Author portrait"></div>
  <p class="author-bio">Owen Farrowdale has provided financial advice since 1998 in areas of investment management, Social Security, tax, retirement planning and wealth transfer strategies.<br>Owen believes that complexity is the enemy of successful financial planning.</p>

  <div class="publisher-mark">
    <span class="publisher-dot"></span>
    <span class="publisher-name">ALDERBROOK PLANNING</span>
  </div>

  <h1 class="front-title">
    <span class="title-lead">Lanterns Over The Quiet</span>
    <span class="title-emphasis title-emphasis-main">MEADOW</span>
    <span class="title-emphasis title-emphasis-sub">WATERS</span>
  </h1>

  <div class="author-block">
    <div class="author-name">OWEN FARROWDALE</div>
    <div class="author-site">www.alderbrookplanning.com</div>
  </div>
</main>
</body>
</html>
```